Marlow's Voyage Handbook Mobile App

We need a sleek new design for our new mobile app we are launching in the South Pacific. This app will be released for both Zelphone and Quorvex. The app has already been developed and your new design will give it the finishing touch we need to release it to our audience. This will be the premiere tourism app for the South Pacific and will be advertised heavily in our successful print publications which are distributed internationally. We are looking for you to provide two designs (for two screens in our mobile app) for this competition. The selected winner will have the opportunity to design the remaining screens in our app and website as a separate contract.

Attached you will see a few of the screens that currently exist in our mobile app to give you a feel for the functionality. The two screens we want you to design for this competition are the main listing page and the category selection page. These two screens will be included in the uploaded files and will be clearly marked so you know what we are looking for.

Please feel free to reach out to us with any questions if you need any guidance in directing your designs. Show us something sleek, engaging, and ultimately something that will drive our users to want to engage with the businesses that are listed in the app.

Please see the uploaded files for a couple of our current designs, the two screens we want you to design for this competition, and a few samples of design ideas we like.

Best of Luck!

Target Market(s)

Travelers to the South Pacific

Industry/Entity Type

Travel Industry

Font styles to use
Serif
Sans Serif

Colors
0492cd
33a6d7
ec1f27
f04a50
85cae6
cee9f5
f59296
cedeed
fbd4d5

Requirements
Must have
• Clean, attractive design for the two screens mentioned in the brief.
Nice to have
• Icon sets, color guide, font selection
Should not have
• Project should not be too busy or incorporate too many different colors, styles, fonts, etc.

```html
<!DOCTYPE html>
<html lang="en">
<head>
<meta charset="utf-8">
<title>Marlow's Voyage Handbook – Category Selection</title>
<link href="https://fonts.googleapis.com/css2?family=Open+Sans:wght@300;400&display=swap" rel="stylesheet">
<style>
  :root {
    --page-bg: #111111;
    --ink: #ffffff;
    --ink-soft: rgba(255,255,255,0.92);
    --scene-top: #5866c8;
    --scene-upper: #5470c0;
    --scene-mid: #4c7fb9;
    --scene-lower: #2f9bc6;
    --scene-bottom: #2d93c6;
  }
  * { box-sizing: border-box; margin: 0; padding: 0; }
  html, body {
    width: 1200px; height: 1200px; overflow: hidden;
    background: var(--page-bg);
    font-family: "Open Sans", Arial, sans-serif;
    color: var(--ink);
  }
  .app-screen {
    position: absolute; left: 287px; top: 42px;
    width: 626px; height: 1115px; overflow: hidden;
  }
  .scene-backdrop {
    position: absolute; inset: 0;
    background: linear-gradient(180deg, var(--scene-top) 0%, var(--scene-upper) 30%, var(--scene-mid) 58%, var(--scene-lower) 80%, var(--scene-bottom) 100%);
  }
  .status-bar {
    position: absolute; top: 10px; left: 15px; right: 14px; height: 24px;
    display: flex; align-items: center; justify-content: space-between;
    font-size: 17px; font-weight: 400;
  }
  .status-left, .status-right { display: flex; align-items: center; gap: 6px; }
  .status-time { position: absolute; left: 50%; transform: translateX(-50%); }
  .app-header { position: absolute; top: 44px; left: 0; right: 0; height: 60px; }
  .menu-toggle { position: absolute; left: 14px; top: 14px; width: 30px; height: 24px; }
  .screen-title {
    position: absolute; left: 0; right: 0; top: 11px; text-align: center;
    font-size: 32px; font-weight: 300; letter-spacing: 0.2px;
  }
  .island-picker {
    position: absolute; right: 14px; top: 18px;
    font-size: 22px; font-weight: 300; display: flex; align-items: center; gap: 10px;
  }
  .category-list { position: absolute; top: 213px; left: 169px; list-style: none; }
  .category-item { display: flex; align-items: center; height: 98px; margin-bottom: 42.4px; }
  .category-icon {
    width: 98px; height: 98px; border: 1.6px solid var(--ink-soft); border-radius: 50%;
    display: flex; align-items: center; justify-content: center;
  }
  .category-icon svg { width: 58px; height: 58px; fill: none; stroke: var(--ink); stroke-width: 1.6; stroke-linejoin: round; stroke-linecap: round; }
  .category-label { margin-left: 32px; font-size: 25px; font-weight: 300; }
</style>
</head>
<body>
<main class="app-screen">
  <div class="scene-backdrop" role="img" aria-label="Photo of a coastal rock arch with trees above turquoise sea, under a blue-violet tint"></div>

  <div class="status-bar">
    <div class="status-left">
      <svg width="52" height="12" viewBox="0 0 52 12"><g fill="#fff"><circle cx="5" cy="6" r="4.5"/><circle cx="15" cy="6" r="4.5"/><circle cx="25" cy="6" r="4.5"/></g><g fill="none" stroke="#fff"><circle cx="35" cy="6" r="4"/><circle cx="45" cy="6" r="4"/></g></svg>
      <span>KELO</span>
      <svg width="20" height="16" viewBox="0 0 20 16" fill="none" stroke="#fff" stroke-width="2" stroke-linecap="round"><path d="M2 6a12 12 0 0 1 16 0"/><path d="M5 9.5a7.5 7.5 0 0 1 10 0"/><circle cx="10" cy="13" r="1.3" fill="#fff"/></svg>
    </div>
    <span class="status-time">4:21 PM</span>
    <div class="status-right">
      <svg width="12" height="18" viewBox="0 0 12 18" fill="none" stroke="rgba(255,255,255,0.7)" stroke-width="1.4"><path d="M2 5l8 8-4 4V1l4 4-8 8"/></svg>
      <span style="margin-left:8px">100%</span>
      <svg width="40" height="16" viewBox="0 0 40 16"><rect x="1" y="1" width="34" height="14" rx="3" fill="none" stroke="#fff" stroke-width="1.4"/><rect x="3" y="3" width="30" height="10" rx="1.5" fill="#fff"/><rect x="36.5" y="5.5" width="2.5" height="5" rx="1" fill="#fff"/></svg>
    </div>
  </div>

  <header class="app-header">
    <svg class="menu-toggle" viewBox="0 0 30 24" stroke="#fff" stroke-width="1.8"><line x1="0" y1="2" x2="30" y2="2"/><line x1="0" y1="12" x2="30" y2="12"/><line x1="0" y1="22" x2="30" y2="22"/></svg>
    <h1 class="screen-title">Cook Islands</h1>
    <div class="island-picker">Rarotonga
      <svg width="14" height="9" viewBox="0 0 14 9" fill="none" stroke="#fff" stroke-width="1.5"><path d="M1 1l6 6 6-6"/></svg>
    </div>
  </header>

  <ul class="category-list">
    <li class="category-item">
      <span class="category-icon"><svg viewBox="0 0 48 48"><path d="M4 24l11-9 11 9"/><path d="M7 22v17h16V22"/><rect x="11" y="30" width="6" height="9"/><path d="M22 14l10-8 10 8v25H23"/><rect x="27" y="16" width="4" height="4"/><rect x="34" y="16" width="4" height="4"/><rect x="27" y="24" width="4" height="4"/><rect x="34" y="24" width="4" height="4"/><line x1="2" y1="39" x2="46" y2="39"/></svg></span>
      <span class="category-label">Accomodations</span>
    </li>
    <li class="category-item">
      <span class="category-icon"><svg viewBox="0 0 48 48"><rect x="4" y="10" width="40" height="24" rx="5"/><rect x="8" y="14" width="32" height="9"/><line x1="16" y1="14" x2="16" y2="23"/><line x1="24" y1="14" x2="24" y2="23"/><line x1="32" y1="14" x2="32" y2="23"/><line x1="4" y1="28" x2="44" y2="28"/><circle cx="13" cy="36" r="3"/><circle cx="35" cy="36" r="3"/></svg></span>
      <span class="category-label">Transportation</span>
    </li>
    <li class="category-item">
      <span class="category-icon"><svg viewBox="0 0 48 48"><path d="M6 16h16l-2 26H8z"/><path d="M14 16l2-8h5"/><path d="M22 30a10 8 0 0 1 20 0z"/><path d="M21 34h22"/><path d="M22 38h20l-2 4H24z"/></svg></span>
      <span class="category-label">Food / Drink</span>
    </li>
    <li class="category-item">
      <span class="category-icon"><svg viewBox="0 0 48 48"><circle cx="11" cy="30" r="8"/><circle cx="37" cy="30" r="8"/><path d="M11 30l7-12h14l5 12"/><path d="M18 18l6 12 8-12"/><path d="M16 14h6"/><path d="M30 18l-1-5h5"/></svg></span>
      <span class="category-label">Activities</span>
    </li>
    <li class="category-item">
      <span class="category-icon"><svg viewBox="0 0 48 48"><path d="M8 18h32v5a4 4 0 0 0 0 8v5H8v-5a4 4 0 0 0 0-8z"/><path d="M14 18l18-8 3 8"/><line x1="20" y1="33" x2="29" y2="21"/><circle cx="21" cy="23" r="2"/><circle cx="28" cy="31" r="2"/></svg></span>
      <span class="category-label">Coupons</span>
    </li>
    <li class="category-item">
      <span class="category-icon"><svg viewBox="0 0 48 48"><path d="M24 40L8 24a9 9 0 0 1 16-11 9 9 0 0 1 16 11z"/></svg></span>
      <span class="category-label">Favorites</span>
    </li>
  </ul>
</main>
</body>
</html>
```